Tarrowby Consulting needs a Business Catalogue

We are looking at creating a business catalogue that is used to introduce ourselves and our business as well as the services we offer. We are an HR business that offers assistance with recruitment and selection and all services involved in that area. We don't offer specific products and don't have prices advertised. it would be good to start with an introduction to the business and our history, some staff bios then a framework to discuss business scenarios where we can help. I would prefer white as the main colour on the front/back page with the colours of the logo (attached) to be used throughout the catalogue along with images and other visual improvements. A mall amount of colour should be used throughout and don't want solid colour pages. Prefer what pages that are broken up by coloured designs, images, diagrams heading etc. A 12-page catalogue with different designs I can move around as needed would be good.

Target Market(s)

Education, government, large business with administration staff

Font styles to use
Sans Serif

Requirements
Must have
• Logo colour scheme
• Images, diagrams, tables etc
• Start with company introduction (history, three staff profiles, company values etc)
• Main section will be the description of services and processes offered.
Nice to have
• A range of different visuals to choose from including designs for tables, paragraphs, diagrams, space for photos and other visual elements.

```html
<!DOCTYPE html>
<html lang="en">
<head>
<meta charset="utf-8">
<title>Tarrowby Consulting – Catalogue Spread</title>
<link href="https://fonts.googleapis.com/css2?family=Ubuntu:ital,wght@0,400;0,500;0,700;1,400&display=swap" rel="stylesheet">
<style>
  :root {
    --blue: #1a96d4;
    --orange: #e6863a;
    --green: #22a24b;
    --ink: #1d1d1b;
    --paper: #ffffff;
  }
  * { margin: 0; padding: 0; box-sizing: border-box; }
  html, body { width: 1200px; height: 848px; overflow: hidden; background: var(--paper); }
  body { font-family: "Ubuntu", "Helvetica Neue", Arial, sans-serif; color: var(--ink); }
  .spread { position: relative; width: 1200px; height: 848px; overflow: hidden; background: var(--paper); }

  .sidebar {
    position: absolute; left: 0; top: 0; width: 212px; height: 779px;
    background: var(--blue); color: var(--paper);
    padding: 127px 16px 0 34px;
  }
  .sidebar h2 { font-size: 16px; font-weight: 700; letter-spacing: .3px; margin-bottom: 18px; }
  .sidebar p { font-size: 10.6px; line-height: 14.4px; margin-bottom: 14.4px; }
  .steps { list-style: none; margin-top: 22px; }
  .steps li { display: flex; align-items: center; height: 44px; }
  .step-num { width: 39px; font-size: 32px; font-weight: 400; color: var(--orange); line-height: 1; }
  .step-text { font-size: 10.6px; line-height: 14.4px; }

  .hero { position: absolute; left: 0; top: 0; }

  .title {
    position: absolute; left: 641px; top: 414px;
    font-size: 40px; font-weight: 700; color: var(--green); letter-spacing: .5px;
  }
  .lead-label {
    position: absolute; left: 251px; top: 470px;
    font-size: 10.6px; font-weight: 700; color: var(--green);
  }
  .lead-quote {
    position: absolute; left: 641px; top: 470px;
    font-size: 10.6px; font-style: italic;
  }
  .column {
    position: absolute; top: 500px;
    font-size: 10.6px; line-height: 14.3px; hyphens: auto;
  }
  .column p { margin-bottom: 14.3px; }
  .column--a { left: 251px; width: 300px; }
  .column--b { left: 641px; width: 246px; }
  .column--c { left: 911px; width: 246px; }

  .footer { position: absolute; left: 0; top: 779px; }
  .folio {
    position: absolute; top: 803px; color: var(--paper);
    display: flex; align-items: center; gap: 8px;
  }
  .folio-num { font-size: 15px; }
  .folio-label { font-size: 8.5px; font-weight: 500; letter-spacing: .2px; }
  .folio--left { left: 32px; }
  .folio--right { right: 34px; }
</style>
</head>
<body>
<div class="spread">

  <svg class="hero" width="1200" height="430" viewBox="0 0 1200 430" role="img" aria-label="Blurred office interior photograph">
    <defs>
      <linearGradient id="heroBase" x1="0" y1="0" x2="1" y2="1">
        <stop offset="0" stop-color="#e4ebf0"/>
        <stop offset=".5" stop-color="#d4dde3"/>
        <stop offset="1" stop-color="#6c7c88"/>
      </linearGradient>
      <radialGradient id="heroDarkLeft" cx="0.12" cy="0.55" r="0.28">
        <stop offset="0" stop-color="#3a4550" stop-opacity=".9"/>
        <stop offset="1" stop-color="#3a4550" stop-opacity="0"/>
      </radialGradient>
      <radialGradient id="heroDarkRight" cx="0.85" cy="0.45" r="0.3">
        <stop offset="0" stop-color="#55626d" stop-opacity=".85"/>
        <stop offset="1" stop-color="#55626d" stop-opacity="0"/>
      </radialGradient>
      <radialGradient id="heroLight" cx="0.42" cy="0.25" r="0.3">
        <stop offset="0" stop-color="#ffffff" stop-opacity=".95"/>
        <stop offset="1" stop-color="#ffffff" stop-opacity="0"/>
      </radialGradient>
      <linearGradient id="heroFloor" x1="0" y1="0" x2="0" y2="1">
        <stop offset=".55" stop-color="#4a5864" stop-opacity="0"/>
        <stop offset="1" stop-color="#4a5864" stop-opacity=".7"/>
      </linearGradient>
    </defs>
    <g>
      <polygon points="212,0 1200,0 1200,384 455,384 428,423 212,423" fill="url(#heroBase)"/>
      <polygon points="212,0 1200,0 1200,384 455,384 428,423 212,423" fill="url(#heroFloor)"/>
      <polygon points="212,0 1200,0 1200,384 455,384 428,423 212,423" fill="url(#heroLight)"/>
      <polygon points="212,0 1200,0 1200,384 455,384 428,423 212,423" fill="url(#heroDarkLeft)"/>
      <polygon points="212,0 1200,0 1200,384 455,384 428,423 212,423" fill="url(#heroDarkRight)"/>
    </g>
  </svg>

  <aside class="sidebar">
    <h2>WELCOME</h2>
    <p>“Neque porro quisquam est<br>qui dolorem ipsum quia dolor<br>sit amet, consectetur, adipisci<br>velit...”</p>
    <p>“There is no one who loves pain<br>itself, who seeks after it and<br>wants to have it, simply because<br>it is pain...”</p>
    <p>Lorem ipsum dolor sit amet,<br>consectetur adipiscing elit.<br>Maecenas commodo sem a<br>sodales ultrices. Curabitur quis<br>libero pretium, congue tellus ac,<br>ullamcorper libero. Phasellus<br>vitae ullamcorper sem. Donec<br>mollis varius mattis. Nulla tortor<br>arcu, maximus varius ultrices<br>quis, vulputate at ligula. Curabi-<br>tur vehicula vel ligula id placerat.<br>Suspendisse tempor nunc eget<br>nibh suscipit imperdiet.</p>
    <p>“Neque porro quisquam est<br>qui dolorem ipsum quia dolor<br>sit amet, consectetur, adipisci<br>velit...”</p>
    <ol class="steps">
      <li><span class="step-num">1</span><span class="step-text">Lorem ipsum dolor sit<br>amet, consectetur elit.</span></li>
      <li><span class="step-num">2</span><span class="step-text">Maecenas commodo<br>sem a sodales ultrices.</span></li>
      <li><span class="step-num">3</span><span class="step-text">Lorem ipsum dolor sit<br>amet, consectetur elit.</span></li>
      <li><span class="step-num">4</span><span class="step-text">Maecenas commodo<br>sem a sodales ultrices.</span></li>
    </ol>
  </aside>

  <h1 class="title">Lorem ipsum</h1>
  <p class="lead-label">Lorem ipsum dolor sit amet</p>
  <p class="lead-quote">“Neque porro quisquam est qui dolorem ipsum quia dolor sit amet, consectetur, adipisci velit...”</p>

  <div class="column column--a">
    <p>Lorem ipsum dolor sit amet, consectetur adipiscing elit. Mae-cenas commodo sem a sodales ultrices. Curabitur quis libero pretium, congue tellus ac, ullamcorper libero. Phasellus vitae ullamcorper sem. Donec mollis varius mattis. Nulla tortor arcu, maximus varius ultrices quis, vulputate at ligula. Curabitur vehicula vel ligula id placerat. Suspendisse tempor nunc eget nibh suscipit imperdiet.</p>
    <p>Nam sed ullamcorper elit. Sed at metus diam. Nunc et massa in velit convallis lacinia. Curabitur odio neque, egestas a augue vel, congue commodo leo. In pharetra augue sit amet arcu ul-tricies ultrices. Lorem ipsum dolor sit amet, consectetur adip-iscing elit. Morbi non euismod leo. Integer a nisl dolor. Cras nec pellentesque lectus. Vivamus efficitur neque in dictum gravida. Nullam a leo nec risus semper tempus. Mauris interdum tellus eu porta commodo. Phasellus eros massa, laoreet vitae tellus eu, ullamcorper varius dui. Etiam in lacus libero. Donec eget massa a urna pretium aliquam.</p>
  </div>

  <div class="column column--b">
    <p>Lorem ipsum dolor sit amet, consectetur adipisc-ing elit. Maecenas commodo sem a sodales ul-trices. Curabitur quis libero pretium, congue tellus ac, ullamcorper libero. Phasellus vitae ullamcorper sem. Donec mollis varius mattis. Nulla tortor arcu, maximus varius ultrices quis, vulputate at ligula. Curabitur vehicula vel ligula id placerat. Suspen-disse tempor nunc eget nibh suscipit imperdiet.</p>
    <p>Nam sed ullamcorper elit. Sed at metus diam. Nunc et massa in velit convallis lacinia. Curabitur odio neque, egestas a augue vel, congue commo-do leo. In pharetra augue sit amet arcu ultricies ultrices. Lorem ipsum dolor sit amet, consectetur adipiscing elit. Morbi non euismod leo. Integer a nisl dolor. Cras nec pellentesque lectus. Vivamus efficitur neque in dictum gravida. Nullam a leo nec risus semper tempus. Mauris interdum tellus eu</p>
  </div>

  <div class="column column--c">
    <p>porta commodo. Phasellus eros massa, laoreet vitae tellus eu, ullamcorper varius dui. Etiam in lacus libero. Donec eget massa a urna pretium aliquam.</p>
    <p>Aliquam dapibus tincidunt facilisis. Ut ut nulla dolor. Etiam vel purus nisi. Praesent elementum cursus justo vel luctus. Donec vitae dapibus quam. Duis eget augue vel sapien consectetur ullamcorper vehicula quis nulla. Nullam dolor la-cus, hendrerit eu auctor ac, viverra in arcu. Integer bibendum rhoncus nisl, id mollis tortor fermen-tum ac. Quisque id velit consequat dui vulputate rutrum. Nulla vulputate leo congue elit bibendum, id rutrum tortor sodales. Cras cursus vel eros vel finibus.</p>
  </div>

  <svg class="footer" width="1200" height="69" viewBox="0 779 1200 69" aria-hidden="true">
    <path d="M0,779 H280 L307,818 H892 L919,779 H1200 V848 H0 Z" fill="var(--orange)"/>
    <rect x="599.5" y="818" width="1" height="30" fill="#ffffff"/>
  </svg>

  <div class="folio folio--left"><span class="folio-num">2</span><span class="folio-label">TARROWBY CONSULTING</span></div>
  <div class="folio folio--right"><span class="folio-label">www.TARROWBY.com</span><span class="folio-num">3</span></div>

</div>
</body>
</html>
```